Meadowlark Learning Support Partners (MLSP)

This is a professional business card. Logo and picture are a must on the front of the card. I am an educational consultant. I have been consulting for the past three years for a company. I am now opening my own company. My goal for my consulting company is to eventually consult all over America.

Target Market(s)

Educators, schools, professionals

Industry/Entity Type

Consulting

Contact Information for Business Card

Picture/logo on front, simple modern design

Font styles to use
Serif

Colors
85abd2
0355a3
3176b5
cedeed

Requirements
Must have
• picture, logo,
• Dorotea Halvorsen, Ed.S
• address 5327 Quarry ridge Ln. Nashville, TN 37058
• Cell:616-555-0182
• Office: 629-555-0147
• www.Mlspwx.com
• halvorsendorotea@mailvexo.com

```html
<!DOCTYPE html>
<html lang="en">
<head>
<meta charset="utf-8">
<title>Meadowlark Learning Support Partners — Business Card</title>
<link href="https://fonts.googleapis.com/css2?family=Montserrat:wght@600;700&family=Roboto+Condensed:wght@700&family=Roboto:wght@400;700&display=swap" rel="stylesheet">
<style>
  :root {
    --stage: #2a2b2d;
    --card-light: #f7f7f6;
    --card-dark: #1c1d20;
    --brand-navy: #0a3d7d;
    --brand-blue: #0d3a73;
    --text-grey: #4a4a4a;
    --url-light: #e2e2e2;
  }
  html, body {
    margin: 0;
    padding: 0;
    width: 1200px;
    height: 960px;
    overflow: hidden;
    background: var(--stage);
  }
  .canvas {
    position: relative;
    width: 1200px;
    height: 960px;
  }
  .card {
    position: absolute;
    left: 320px;
    width: 600px;
    box-sizing: border-box;
  }
  .card--front {
    top: 100px;
    height: 345px;
    background: var(--card-light);
  }
  .card--back {
    top: 493px;
    height: 342px;
    background: var(--card-dark);
  }
  .front-mark {
    position: absolute;
    left: 88px;
    top: 206px;
    width: 132px;
    text-align: center;
    font-family: "Roboto", sans-serif;
    font-weight: 700;
    font-size: 40px;
    letter-spacing: 3px;
    line-height: 1;
    color: var(--brand-navy);
  }
  .front-divider {
    position: absolute;
    left: 252px;
    top: 85px;
    width: 2px;
    height: 195px;
    background: linear-gradient(to bottom, rgba(10,61,125,0), var(--brand-navy) 30%, var(--brand-navy) 70%, rgba(10,61,125,0));
  }
  .contact {
    position: absolute;
    left: 278px;
    top: 102px;
    font-family: "Roboto", sans-serif;
    color: var(--text-grey);
  }
  .contact__name {
    margin: 0 0 22px;
    font-family: "Roboto Condensed", sans-serif;
    font-weight: 700;
    font-size: 21px;
    letter-spacing: 0.2px;
    color: var(--brand-navy);
  }
  .contact__address {
    margin: 0 0 12px;
    font-size: 14.5px;
    line-height: 18px;
    font-style: normal;
  }
  .contact__list {
    list-style: none;
    margin: 0;
    padding: 0;
    font-size: 14.5px;
    line-height: 19px;
  }
  .contact__list li {
    display: flex;
    align-items: center;
    gap: 8px;
  }
  .contact__icon {
    width: 13px;
    height: 13px;
    fill: var(--brand-navy);
    flex: none;
  }
  .back-lockup {
    position: absolute;
    left: 220px;
    top: 134px;
    display: flex;
    align-items: center;
  }
  .back-mark {
    font-family: "Roboto", sans-serif;
    font-weight: 700;
    font-size: 24px;
    letter-spacing: 2px;
    color: var(--brand-blue);
    padding-right: 12px;
    border-right: 2px solid var(--brand-blue);
    line-height: 72px;
  }
  .back-tagline {
    margin: 0 0 0 11px;
    font-family: "Montserrat", sans-serif;
    font-weight: 600;
    font-size: 14px;
    line-height: 19.5px;
    color: var(--brand-blue);
  }
  .back-url {
    position: absolute;
    left: 0;
    right: 0;
    top: 287px;
    text-align: center;
    font-family: "Roboto", sans-serif;
    font-size: 15px;
    letter-spacing: 0.6em;
    color: var(--url-light);
  }
</style>
</head>
<body>
<main class="canvas">
  <section class="card card--front" aria-label="Business card front">
    <div class="front-mark">MLSP</div>
    <div class="front-divider"></div>
    <div class="contact">
      <h1 class="contact__name">DOROTEA HALVORSEN, ED.S</h1>
      <address class="contact__address">5327 Quarry ridge Ln.<br>Nashville, TN 37058</address>
      <ul class="contact__list">
        <li><svg class="contact__icon" viewBox="0 0 16 16"><path d="M3.6 1.2l2.3 2.6-1.3 1.8c.8 1.9 2.2 3.3 4.1 4.2l1.8-1.3 2.6 2.3-1.3 2.6C6.5 13.2 2.6 9.3 1.2 3.6z"/></svg>629-555-0147</li>
        <li><svg class="contact__icon" viewBox="0 0 16 16"><path d="M4.5 0.5h7a1 1 0 0 1 1 1v13a1 1 0 0 1-1 1h-7a1 1 0 0 1-1-1v-13a1 1 0 0 1 1-1zM5 2.5v9.5h6V2.5zM8 12.8a.9.9 0 1 0 0 1.8.9.9 0 0 0 0-1.8z"/></svg>616-555-0182</li>
        <li><svg class="contact__icon" viewBox="0 0 16 16"><path d="M1 3.5h14v9H1zM2.3 4.5L8 9l5.7-4.5z"/></svg>halvorsendorotea@mailvexo.com</li>
        <li><svg class="contact__icon" viewBox="0 0 16 16"><circle cx="8" cy="8" r="7"/><path d="M4 5.5c1.5-.5 2.5.5 2.2 1.6-.3 1 .8 1.5.6 2.8-.1.8-1 1.6-.6 3.2M10 3c-.6 1.2.4 2 1.5 2.2 1 .2 1.3 1.2.8 2" stroke="#f7f7f6" stroke-width="1.3" fill="none"/></svg>www.Mlspwx.com</li>
      </ul>
    </div>
  </section>

  <section class="card card--back" aria-label="Business card back">
    <div class="back-lockup">
      <div class="back-mark">MLSP</div>
      <p class="back-tagline">Meadowlark<br>Learning<br>Support<br>Partners</p>
    </div>
    <div class="back-url">www.Mlspwx.com</div>
  </section>
</main>
</body>
</html>
```